New Business Card Design Project

Easy part first... I want the backside to be simple... jet black background with our logo in jet black/white/color. Feel free to play with tagline ideas under the logo if you want, I'm still toying around with it myself.

The front side... I need the logo on it, my photo headshot, and the following information:

Ray T. Calloway
Top Producer
555-201-4837
calloway.ray.t@fernmail.example
www.listnorthernnests.example
www.getnorthernnests.example

I'm looking for creativity with font, simple, but elegant, pairs well with the logo, good visibility of my photo, black background on the front as well, clearly see and identify information.
Updates

I would like the websites to have capitalization on the first letter of each word - www.ListNorthernNests.example and www.GetNorthernNests.example Also, I would like each of the capital letters to be slightly larger than the other font

Target Market(s)

We help people buy and sell homes from $50,000 to over a $1million.

Industry/Entity Type

Business

Requirements
Must have
• Must have information from above.
Nice to have
• Introducing a new color to be sharp against the black- possibly in the silver/nickel/platinum metallics? Feel free to crop the headshot down some if needed.
Should not have
• NO CHEESY GRAPHICS

```html
<!DOCTYPE html>
<html lang="en">
<head>
<meta charset="utf-8">
<title>Nest Hollow Realty – Business Card</title>
<link rel="stylesheet" href="https://fonts.googleapis.com/css2?family=Montserrat:wght@400;600;700&display=swap">
<style>
  :root {
    --page-bg: #d9d6d0;
    --card-black: #050505;
    --ink-white: #f4f4f2;
    --khaki: #b3a566;
    --amber: #e9a51a;
    --ink-dark: #141414;
    --photo-top: #2a2c30;
    --photo-bottom: #3d4a63;
  }
  * { margin: 0; padding: 0; box-sizing: border-box; }
  html, body {
    width: 1200px; height: 900px; overflow: hidden;
    background: var(--page-bg);
    font-family: "Montserrat", sans-serif;
  }
  .canvas {
    width: 1200px; height: 900px;
    display: flex; flex-direction: column; align-items: center; justify-content: center;
    gap: 40px;
  }
  .card {
    width: 700px; height: 400px;
    position: relative; overflow: hidden;
    background: var(--card-black);
    box-shadow: 0 10px 30px rgba(0,0,0,.25);
  }
  .card-art { position: absolute; inset: 0; width: 100%; height: 100%; }

  /* Back */
  .card-back { display: flex; align-items: center; justify-content: center; }
  .brand-lockup { display: flex; align-items: center; gap: 14px; }
  .brand-mark { width: 16px; height: 16px; background: var(--khaki); flex: none; }
  .brand-name {
    color: var(--ink-white); font-weight: 600; letter-spacing: .18em;
    text-transform: uppercase; font-size: 26px; white-space: nowrap;
  }

  /* Front */
  .front-brand { position: absolute; left: 110px; top: 52px; }
  .front-brand .brand-name { font-size: 17px; }
  .front-brand .brand-mark { width: 11px; height: 11px; }
  .contact-list {
    position: absolute; left: 64px; top: 104px;
    list-style: none; color: var(--ink-white);
    font-size: 12.5px; letter-spacing: .06em;
  }
  .contact-list li { display: flex; align-items: center; gap: 12px; height: 21px; white-space: nowrap; }
  .contact-icon { width: 11px; height: 11px; flex: none; display: block; }
  .cap { font-size: 1.12em; }
  .agent {
    position: absolute; left: 392px; top: 336px; color: var(--ink-dark);
  }
  .agent-name { font-size: 20px; font-weight: 700; letter-spacing: .16em; white-space: nowrap; }
  .agent-title { font-size: 13px; font-weight: 400; letter-spacing: .12em; margin-top: 2px; }
</style>
</head>
<body>
<main class="canvas">

  <section class="card card-back" aria-label="Card back">
    <div class="brand-lockup">
      <span class="brand-mark"></span>
      <span class="brand-name">Nest Hollow Realty</span>
    </div>
  </section>

  <section class="card card-front" aria-label="Card front">
    <svg class="card-art" viewBox="0 0 700 400" preserveAspectRatio="none">
      <defs>
        <linearGradient id="photoTone" x1="0" y1="0" x2="0" y2="1">
          <stop offset="0" stop-color="#2a2c30"/>
          <stop offset="1" stop-color="#3d4a63"/>
        </linearGradient>
      </defs>
      <rect class="headshot" x="340" y="140" width="320" height="260" fill="url(#photoTone)"
            role="img" aria-label="Headshot of Ray T. Calloway in a dark suit and blue tie"/>
      <path class="accent-stripe" fill="#e9a51a"
            d="M0,222 C150,286 350,338 700,356 L700,400 L0,400 Z"/>
      <path class="name-band" fill="#b3a566"
            d="M0,232 C150,296 350,348 700,366 L700,400 L0,400 Z"/>
    </svg>

    <div class="front-brand brand-lockup">
      <span class="brand-mark"></span>
      <span class="brand-name">Nest Hollow Realty</span>
    </div>

    <ul class="contact-list">
      <li>
        <svg class="contact-icon" viewBox="0 0 12 12"><path d="M2.5 1 L4.5 1 L5.3 3.6 L4 4.6 C4.6 6 6 7.4 7.4 8 L8.4 6.7 L11 7.5 L11 9.5 C11 10.3 10.3 11 9.5 11 C5 11 1 7 1 2.5 C1 1.7 1.7 1 2.5 1 Z" fill="#e9a51a"/></svg>
        <span>555-201-4837</span>
      </li>
      <li>
        <svg class="contact-icon" viewBox="0 0 12 12"><rect x="1" y="2.5" width="10" height="7" fill="none" stroke="#e9a51a" stroke-width="1.2"/><path d="M1 2.5 L6 6.5 L11 2.5" fill="none" stroke="#e9a51a" stroke-width="1.2"/></svg>
        <span>calloway.ray.t@fernmail.example</span>
      </li>
      <li>
        <svg class="contact-icon" viewBox="0 0 12 12"><circle cx="6" cy="6" r="4.8" fill="none" stroke="#e9a51a" stroke-width="1.2"/><path d="M1.2 6 H10.8 M6 1.2 C3.8 4 3.8 8 6 10.8 M6 1.2 C8.2 4 8.2 8 6 10.8" fill="none" stroke="#e9a51a" stroke-width="1"/></svg>
        <span>www.<span class="cap">L</span>ist<span class="cap">N</span>orthern<span class="cap">N</span>ests.example</span>
      </li>
      <li>
        <svg class="contact-icon" viewBox="0 0 12 12"><circle cx="6" cy="6" r="4.8" fill="none" stroke="#e9a51a" stroke-width="1.2"/><path d="M1.2 6 H10.8 M6 1.2 C3.8 4 3.8 8 6 10.8 M6 1.2 C8.2 4 8.2 8 6 10.8" fill="none" stroke="#e9a51a" stroke-width="1"/></svg>
        <span>www.<span class="cap">G</span>et<span class="cap">N</span>orthern<span class="cap">N</span>ests.example</span>
      </li>
    </ul>

    <div class="agent">
      <div class="agent-name">Ray T. Calloway</div>
      <div class="agent-title">Top Producer</div>
    </div>
  </section>

</main>
</body>
</html>
```